Verpackungsdesign für Outdoor-Produkt
Lurvo suchte ein neues Design in der Kategorie Verpackungen und hat ein Projekt auf gestaltwerk-portal.de gestartet.
Zielgruppe
Wir verkaufen einzigartige Outdoor Produkte. Der Feuerstahl richtet sich an alle, die gerne in der Natur übernachten und beim Feuermachen noch selbst Hand anlegen wollen. Die Zielgruppe interessiert sich für Bushcraft & Survival, ist größtenteils Männlich und zwischen 30-40 Jahre alt.
Aufgabenstellung
Auf die obere Seite der Verpackung sollen das Logo und der Produktname platziert werden. Das Produkt gibt es in zwei Varianten, deshalb auch zwei verschiedene Namen.
Auf der vorderen Seite sollen die Features hervorgehoben werden. Dafür zum Beispiel ein passendes Icon finden und die Eigenschaft dazu (Beispiel: 'Flammen'-Icon, Bis zu 20.000 Zündungen garantiert).
An den Seiten links und rechts reicht das Logo.
Auf die hintere Seite kommt das Impressum.
Die Verpackung besteht aus braunem Karton.

```html
<!DOCTYPE html>
<html lang="de">
<head>
<meta charset="utf-8">
<title>Lurvo Feuerstahl – Verpackung Stanzkontur</title>
<link href="https://fonts.googleapis.com/css2?family=Roboto+Slab:wght@300;400;500;700&family=Open+Sans:wght@400&display=swap" rel="stylesheet">
<style>
  :root {
    --paper: #ffffff;
    --ink: #111111;
    --cut: #1a1a1a;
    --crease: #e8312f;
    --caption: #a9a9a9;
  }
  html, body { margin: 0; padding: 0; overflow: hidden; background: var(--paper); }
  .sheet { width: 873px; height: 1200px; position: relative; background: var(--paper); }
  .sheet svg { display: block; width: 873px; height: 1200px; }
  .cut { fill: none; stroke: var(--cut); stroke-width: 1.3; stroke-linejoin: round; }
  .crease { stroke: var(--crease); stroke-width: 1.1; fill: none; }
  .icon { fill: none; stroke: var(--ink); stroke-width: 2; stroke-linecap: round; stroke-linejoin: round; }
  .txt { font-family: "Roboto Slab", serif; fill: var(--ink); }
  .imprint { font-size: 12px; font-weight: 400; }
  .imprint-strong { font-weight: 700; }
  .brand-name { font-size: 46px; font-weight: 700; letter-spacing: 4px; }
  .product-name { font-size: 26px; font-weight: 700; letter-spacing: 0.5px; }
  .product-variant { font-size: 22px; font-weight: 300; }
  .feature-title { font-size: 12.5px; font-weight: 500; }
  .feature-text { font-size: 9.8px; font-weight: 400; }
  .caption { font-family: "Open Sans", sans-serif; font-size: 12px; letter-spacing: 1.6px; fill: var(--caption); }
</style>
</head>
<body>
<div class="sheet">
<svg viewBox="0 0 1600 2200" xmlns="http://www.w3.org/2000/svg" aria-label="Stanzkontur der Faltschachtel Feuerstahl Basic">

  <!-- cut outline: lid with tuck flap -->
  <g class="dieline">
    <path class="cut" d="M403,162 L1197,162 L1205,168 C1262,176 1297,205 1297,232 L1297,280 Q1297,295 1282,295 L1213,295 L1197,305 M403,162 L395,168 C338,176 303,205 303,232 L303,280 Q303,295 318,295 L387,295 L403,305"/>
    <!-- back panel -->
    <path class="cut" d="M403,305 L395,313 L395,512 L407,520 M1197,305 L1205,313 L1205,512 L1193,520"/>
    <!-- inner panel with dust flaps -->
    <path class="cut" d="M407,520 L395,531 L307,531 L307,653 L400,653 Q407,653 407,660 L397,665"/>
    <path class="cut" d="M1193,520 L1205,531 L1293,531 L1293,653 L1200,653 Q1193,653 1193,660 L1203,665"/>
    <!-- top panel side flaps -->
    <path class="cut" d="M397,665 L257,665 L237,672 L104,672 L104,740 L86,744 L86,797 L104,801 L104,866 L237,866 L257,872 L413,872"/>
    <path class="cut" d="M1203,665 L1343,665 L1363,672 L1496,672 L1496,740 L1514,744 L1514,797 L1496,801 L1496,866 L1363,866 L1343,872 L1187,872"/>
    <path class="cut" d="M397,738 L417,738 L417,800 L397,800 M1203,738 L1183,738 L1183,800 L1203,800"/>
    <!-- front panel with flaps -->
    <path class="cut" d="M413,872 L405,885 L314,885 L314,1006 L405,1006 L413,1012 L1187,1012 L1195,1006 L1286,1006 L1286,885 L1195,885 L1187,872"/>

    <!-- crease lines -->
    <line class="crease" x1="403" y1="162" x2="403" y2="305"/>
    <line class="crease" x1="1197" y1="162" x2="1197" y2="305"/>
    <line class="crease" x1="403" y1="305" x2="1197" y2="305"/>
    <line class="crease" x1="407" y1="520" x2="1193" y2="520"/>
    <line class="crease" x1="407" y1="520" x2="407" y2="665"/>
    <line class="crease" x1="1193" y1="520" x2="1193" y2="665"/>
    <line class="crease" x1="397" y1="665" x2="1203" y2="665"/>
    <line class="crease" x1="397" y1="665" x2="397" y2="872"/>
    <line class="crease" x1="1203" y1="665" x2="1203" y2="872"/>
    <line class="crease" x1="257" y1="665" x2="257" y2="872"/>
    <line class="crease" x1="237" y1="672" x2="237" y2="866"/>
    <line class="crease" x1="1343" y1="665" x2="1343" y2="872"/>
    <line class="crease" x1="1363" y1="672" x2="1363" y2="866"/>
    <line class="crease" x1="397" y1="872" x2="1203" y2="872"/>
    <line class="crease" x1="413" y1="872" x2="413" y2="1012"/>
    <line class="crease" x1="1187" y1="872" x2="1187" y2="1012"/>
  </g>

  <!-- back panel: imprint -->
  <g class="imprint-block txt" text-anchor="middle">
    <text class="txt imprint imprint-strong" x="800" y="387">Lurvo</text>
    <text class="txt imprint" x="800" y="415">Am Waldrand 12 · 20095 Hamburg · Deutschland</text>
    <text class="txt imprint" x="800" y="443">kundenservice@lurvo.de</text>
    <text class="txt imprint imprint-strong" x="800" y="457">www.lurvo.de</text>
  </g>

  <!-- top panel: brand and product -->
  <g class="top-panel">
    <text class="txt brand-name" x="800" y="790" text-anchor="middle">LURVO</text>
    <text class="txt product-name" x="1172" y="706" text-anchor="end">FEUERSTAHL</text>
    <text class="txt product-variant" x="1172" y="732" text-anchor="end">BASIC</text>
  </g>

  <!-- front panel: features -->
  <g class="features" text-anchor="middle">
    <g class="feature feature-sparks">
      <path class="icon" d="M546,893 C552,901 557,907 557,914 C557,920 552,923 546,923 C540,923 536,920 536,914 C536,908 540,904 541,900 C543,905 545,907 547,908 C548,903 547,898 546,893 Z"/>
      <text class="txt feature-title" x="546" y="944">3000 °C HEIßE</text>
      <text class="txt feature-title" x="546" y="958">FUNKEN</text>
      <text class="txt feature-text" x="546" y="976">Mehr als 20.000</text>
      <text class="txt feature-text" x="546" y="988">Zündungen garantiert</text>
    </g>
    <g class="feature feature-rod">
      <path class="icon" d="M678,904 L720,913 L718,919 L676,910 Z"/>
      <text class="txt feature-title" x="697" y="944">XXL</text>
      <text class="txt feature-title" x="697" y="958">ZÜNDSTAB</text>
      <text class="txt feature-text" x="697" y="976">12,7 cm lang,</text>
      <text class="txt feature-text" x="697" y="988">1,27 cm Durchmesser</text>
    </g>
    <g class="feature feature-striker">
      <path class="icon" d="M850,918 L878,902 C884,899 889,904 885,909 L862,922 Z M852,916 L856,921"/>
      <circle class="icon" cx="880" cy="906" r="2"/>
      <text class="txt feature-title" x="867" y="944">SURVIVAL STRIKER</text>
      <text class="txt feature-text" x="868" y="964">Hochwertiger 8Cr13MoV Stahl,</text>
      <text class="txt feature-text" x="868" y="976">läßt sich im Notfall sogar zu</text>
      <text class="txt feature-text" x="868" y="988">Mini Messer schärfen</text>
    </g>
    <g class="feature feature-weather">
      <path class="icon" d="M994,905 L1020,905 M1000,912 L1034,912 C1040,912 1040,905 1035,905 M996,918 L1024,918 M1014,899 C1014,896 1018,896 1020,899"/>
      <path class="icon" d="M1055,908 C1050,915 1048,918 1048,920 C1048,924 1058,924 1058,920 C1058,918 1057,915 1055,908 Z M1067,899 C1064,904 1063,906 1063,908 C1063,911 1071,911 1071,908 C1071,906 1070,904 1067,899 Z"/>
      <path class="icon" d="M1096,898 L1096,922 M1086,904 L1106,916 M1086,916 L1106,904 M1092,899 L1096,903 L1100,899 M1092,921 L1096,917 L1100,921"/>
      <text class="txt feature-title" x="1050" y="944">WIND-/WASSER-/</text>
      <text class="txt feature-title" x="1050" y="958">KÄLTE-RESIST</text>
      <text class="txt feature-text" x="1050" y="976">Schutz bei</text>
      <text class="txt feature-text" x="1050" y="988">allen Witterungen</text>
    </g>
  </g>

  <text class="caption" x="800" y="2083" text-anchor="middle">PACKAGING „LURVO“ ABMESSUNG 50 X 35  X 195 MM · WWW.LURVO.DE</text>
</svg>
</div>
</body>
</html>
```